Business Card Ayurvedic Massage

I'm starting with my ayurvedic massage business and need a business card design. The design should be inline with my brand/logo as well as with the design of my website (www.lumo-thara.ch).
Front: logo and text "Ayurvedische Massagen"
back: name and adress (see details https://www.lumo-thara.ch/kontakt.html)

```html
<!DOCTYPE html>
<html lang="de">
<head>
<meta charset="utf-8">
<title>lumo-thara – Visitenkarte</title>
<link href="https://fonts.googleapis.com/css2?family=Tinos:wght@400;700&display=swap" rel="stylesheet">
<style>
  :root {
    --page-bg: #ecebe8;
    --card-red: #a3121c;
    --card-white: #ffffff;
    --gold: #d9a13a;
    --gold-light: #f2d9a0;
    --gold-brown: #a8731f;
    --name-red: #b3121d;
    --shadow: rgba(0, 0, 0, 0.18);
  }
  * { margin: 0; padding: 0; box-sizing: border-box; }
  html, body {
    width: 1200px;
    height: 800px;
    overflow: hidden;
    background: var(--page-bg);
    font-family: "Tinos", "Times New Roman", serif;
  }
  .canvas {
    position: relative;
    width: 1200px;
    height: 800px;
  }
  .card {
    position: absolute;
    top: 232px;
    width: 520px;
    height: 336px;
    border-radius: 22px;
    box-shadow: 0 14px 34px var(--shadow);
    display: flex;
    flex-direction: column;
    align-items: center;
    justify-content: center;
  }
  .card-front {
    left: 50px;
    background: var(--card-red);
  }
  .card-back {
    left: 630px;
    background: var(--card-white);
  }
  .brand-row {
    display: flex;
    align-items: center;
    gap: 10px;
  }
  .brand-dot {
    width: 14px;
    height: 14px;
    border-radius: 50%;
    background: var(--gold);
  }
  .brand-name {
    font-size: 40px;
    font-weight: 700;
    color: var(--gold);
    letter-spacing: 1px;
  }
  .tagline {
    margin-top: 14px;
    font-size: 15px;
    letter-spacing: 1.5px;
    color: var(--gold-light);
    text-transform: uppercase;
  }
  .card-back .brand-name {
    font-size: 32px;
    color: var(--gold-brown);
  }
  .contact {
    margin-top: 14px;
    text-align: center;
    font-size: 13.5px;
    line-height: 1.45;
    color: var(--gold-brown);
  }
  .contact .person {
    font-weight: 700;
    font-size: 15px;
    color: var(--name-red);
    text-transform: uppercase;
    margin-bottom: 2px;
  }
</style>
</head>
<body>
<main class="canvas">
  <section class="card card-front" aria-label="Vorderseite">
    <div class="brand-row">
      <span class="brand-dot"></span>
      <span class="brand-name">lumo-thara</span>
    </div>
    <p class="tagline">Ayurvedische Massagen</p>
  </section>

  <section class="card card-back" aria-label="Rückseite">
    <div class="brand-row">
      <span class="brand-dot"></span>
      <span class="brand-name">lumo-thara</span>
    </div>
    <address class="contact">
      <p class="person">Mira Castell</p>
      <p>lumo-thara, Talweg 12, 8855 Wangen (SZ)</p>
      <p>Phone: +41 77 000 12 34</p>
      <p>E mail: info@lumo-thara.ch</p>
      <p>www.lumo-thara.ch</p>
    </address>
  </section>
</main>
</body>
</html>
```